Wedding Vow Design for Modern Print - SUBWAY PRINT STYLE or Similar, MODERN

I recently got married and I want to take the main words from my wedding vows and create a design using them that I can have printed and present to my new wife. I told her that I had privileges with Marring her and I made her promises. I would like to highlight both. We have a modern home and I want something that we can have professionally framed and hung on the wall. Love modern and clean design but something interesting.

Target Market(s)

Myself. 35, modern and loves clean design.

Industry/Entity Type

Wedding

Font styles to use
Serif

Colors
f6f3f8
ffffff
fbd4d5
000000
9d9d9d
dddddd

Requirements
Must have
• Cool, clean and modern design. Neutral Colors, Clean lines, Black and White, no reds, pinks, etc.
• We will hang this in our California modern home.
Nice to have
• Our wedding colors were , Gray,Black, Light Pink. I love the Subway signs and also love Black and White Word art.
Should not have
• Flowers, squiggly lines, traditional design. Something that would look great in a stainless metal frame or mirrored frame on white walls.

```html
<!DOCTYPE html>
<html lang="en">
<head>
<meta charset="utf-8">
<title>Privileges &amp; Promises</title>
<link rel="stylesheet" href="https://fonts.googleapis.com/css2?family=Amatic+SC:wght@700&family=Montserrat:wght@200;800&family=Playfair+Display:wght@700;900&family=Oswald:wght@500&display=swap">
<style>
  :root {
    --ink: #000000;
    --paper: #ffffff;
    --mist: #dddddd;
    --stone: #9d9d9d;
  }
  * { box-sizing: border-box; margin: 0; padding: 0; }
  html, body { width: 857px; height: 1200px; overflow: hidden; background: var(--paper); }
  .vow-print { position: relative; width: 857px; height: 1200px; background: var(--paper); color: var(--ink); }
  .abs { position: absolute; }
  .line { display: flex; align-items: center; white-space: nowrap; }

  .section-band { left: 15px; width: 820px; height: 88px; }
  .section-band svg { position: absolute; inset: 0; }
  .section-title {
    position: absolute; inset: 0; display: flex; align-items: center; justify-content: center;
    font-family: "Amatic SC", cursive; font-weight: 700; font-size: 66px; color: var(--paper); letter-spacing: 2px;
  }

  .heavy { font-family: "Montserrat", sans-serif; font-weight: 800; }
  .engraved { font-family: "Playfair Display", serif; font-weight: 900; text-transform: uppercase; }
  .hand { font-family: "Amatic SC", cursive; font-weight: 700; }
  .condensed { font-family: "Oswald", sans-serif; font-weight: 500; }

  .life-line { left: 75px; width: 705px; top: 180px; height: 86px; justify-content: center; font-size: 76px; letter-spacing: 1px; }
  .triangle-row { left: 75px; width: 705px; height: 16px; }

  .care-line { left: 75px; top: 318px; width: 705px; height: 52px; justify-content: space-between; font-size: 46px; letter-spacing: 1px; }
  .crossed-mark { width: 34px; height: 52px; background: var(--mist); }

  .regardless-ribbon { left: 78px; top: 400px; width: 700px; height: 62px; }
  .regardless-text { position: absolute; inset: 0; display: flex; align-items: center; justify-content: center; font-size: 46px; letter-spacing: 2px; }

  .virtues-line { left: 75px; top: 495px; width: 705px; height: 52px; justify-content: space-between; font-size: 45px; }
  .virtues-line .light { font-weight: 200; }
  .diamond { width: 9px; height: 9px; background: var(--ink); transform: rotate(45deg); }

  .fight-line { left: 75px; top: 668px; width: 705px; height: 66px; justify-content: space-between; font-size: 50px; letter-spacing: 8px; }
  .seal { width: 74px; height: 74px; }

  .dash-rule { height: 0; border-top: 1.5px dashed var(--ink); }

  .support-line { left: 75px; top: 770px; width: 705px; height: 52px; justify-content: center; gap: 16px; font-size: 45px; }

  .cherish-line { left: 75px; top: 866px; width: 440px; height: 50px; gap: 20px; font-size: 40px; letter-spacing: 1px; }
  .star { width: 22px; height: 22px; }

  .best-box { left: 75px; top: 945px; width: 470px; height: 96px; background: var(--mist); }
  .best-text { position: absolute; left: 22px; top: 4px; font-size: 48px; letter-spacing: 6px; }
  .hearts { position: absolute; left: 182px; top: 74px; display: flex; gap: 8px; }

  .you-me { left: 75px; top: 1052px; width: 470px; height: 62px; font-size: 56px; }
  .you-me .you { position: absolute; left: 65px; }
  .you-me .me { position: absolute; left: 335px; }
  .you-me .divider { position: absolute; left: 262px; top: 8px; height: 46px; border-left: 1.5px dotted var(--ink); }

  .side-pennant { left: 538px; top: 816px; width: 250px; height: 256px; }
  .side-pennant svg { position: absolute; inset: 0; }
  .pointing-hands { position: absolute; left: 28px; top: 40px; width: 170px; height: 40px; background: var(--mist); }
  .pennant-rule { position: absolute; left: 24px; top: 92px; width: 178px; border-top: 2px solid var(--ink); }
  .pennant-text { position: absolute; left: 4px; top: 104px; width: 218px; text-align: center; line-height: 1; }
  .pennant-text .small { font-size: 33px; display: block; }
  .pennant-text .big { font-size: 60px; display: block; }
</style>
</head>
<body>
<main class="vow-print">

  <svg width="0" height="0" style="position:absolute">
    <defs>
      <pattern id="tri-down" width="19" height="16" patternUnits="userSpaceOnUse">
        <polygon points="2,1 15,1 8.5,14" fill="#000"/>
      </pattern>
      <pattern id="tri-up" width="19" height="16" patternUnits="userSpaceOnUse">
        <polygon points="2,15 15,15 8.5,2" fill="#000"/>
      </pattern>
      <pattern id="hatch" width="5" height="5" patternUnits="userSpaceOnUse" patternTransform="rotate(45)">
        <line x1="0" y1="0" x2="0" y2="5" stroke="#000" stroke-width="1.2"/>
      </pattern>
    </defs>
  </svg>

  <header class="section-band abs" style="top:58px">
    <svg viewBox="0 0 820 88" width="820" height="88" preserveAspectRatio="none">
      <path d="M40 4 L790 2 L800 10 L818 14 L796 22 L812 34 L794 44 L816 58 L792 66 L806 78 L780 86 L40 86 L22 80 L36 72 L4 64 L28 54 L10 42 L30 32 L6 22 L30 14 Z" fill="#000"/>
    </svg>
    <h1 class="section-title">PRIVILEGES</h1>
  </header>

  <div class="line life-line heavy abs">REST OF MY LIFE</div>

  <svg class="triangle-row abs" style="top:283px" width="705" height="16"><rect width="705" height="16" fill="url(#tri-down)"/></svg>

  <div class="line care-line engraved abs">
    <span>Protection</span>
    <span class="crossed-mark" role="img" aria-label="Small diamond above crossed arrows ornament"></span>
    <span>Provision</span>
  </div>

  <div class="regardless-ribbon abs">
    <svg viewBox="0 0 700 62" width="700" height="62">
      <polygon points="0,0 700,0 680,31 700,62 0,62 20,31" fill="#dddddd"/>
      <line x1="30" y1="31" x2="158" y2="31" stroke="#000" stroke-width="1" stroke-dasharray="2 2"/>
      <line x1="545" y1="31" x2="672" y2="31" stroke="#000" stroke-width="1" stroke-dasharray="2 2"/>
    </svg>
    <div class="regardless-text hand">LOVE - REGARDLESS</div>
  </div>

  <div class="line virtues-line heavy abs">
    <span>CARE</span><span class="diamond"></span><span class="light">PURPOSE</span><span class="diamond"></span><span>PATIENCE</span>
  </div>

  <header class="section-band abs" style="top:562px">
    <svg viewBox="0 0 820 88" width="820" height="88" preserveAspectRatio="none">
      <path d="M36 6 L786 2 L804 12 L818 20 L798 30 L814 42 L790 52 L812 64 L796 76 L784 86 L44 86 L20 78 L34 68 L2 58 L26 48 L8 36 L30 26 L12 14 Z" fill="#000"/>
    </svg>
    <h2 class="section-title">PROMISES</h2>
  </header>

  <div class="line fight-line engraved abs">
    <svg class="seal" viewBox="0 0 74 74" aria-hidden="true">
      <circle cx="37" cy="37" r="34" fill="none" stroke="#000" stroke-width="5" stroke-dasharray="1 2.2"/>
      <circle cx="37" cy="37" r="24" fill="none" stroke="#000" stroke-width="1.2" stroke-dasharray="2 2"/>
      <path d="M28 27 L37 24 L46 27 L46 38 Q46 47 37 51 Q28 47 28 38 Z" fill="#9d9d9d"/>
    </svg>
    <span>Fight</span>
    <svg class="seal" viewBox="0 0 74 74" aria-hidden="true">
      <circle cx="37" cy="37" r="34" fill="none" stroke="#000" stroke-width="5" stroke-dasharray="1 2.2"/>
      <circle cx="37" cy="37" r="24" fill="none" stroke="#000" stroke-width="1.2" stroke-dasharray="2 2"/>
      <path d="M24 38 Q37 20 50 38 Z" fill="#9d9d9d"/>
      <path d="M37 38 L37 48 Q37 51 34 50" fill="none" stroke="#000" stroke-width="1.5"/>
    </svg>
    <span>Safety</span>
  </div>

  <div class="dash-rule abs" style="left:75px; top:752px; width:705px"></div>

  <div class="line support-line heavy abs"><span>UNCONDITIONAL</span><span>SUPPORT</span></div>

  <div class="dash-rule abs" style="left:75px; top:837px; width:465px"></div>

  <div class="line cherish-line condensed abs">
    <svg class="star" viewBox="0 0 24 24"><polygon points="12,1 15,9 23,9 17,14 19,23 12,18 5,23 7,14 1,9 9,9" fill="#000"/></svg>
    <span>CHERISH</span>
    <svg class="star" viewBox="0 0 24 24"><polygon points="12,1 15,9 23,9 17,14 19,23 12,18 5,23 7,14 1,9 9,9" fill="#000"/></svg>
    <span>LISTEN</span>
    <svg class="star" viewBox="0 0 24 24"><polygon points="12,1 15,9 23,9 17,14 19,23 12,18 5,23 7,14 1,9 9,9" fill="#000"/></svg>
  </div>

  <div class="best-box abs">
    <div class="best-text engraved">The Best In</div>
    <div class="hearts">
      <svg width="14" height="12" viewBox="0 0 14 12"><path d="M7 12 L1 5 Q-1 1 3 0.5 Q6 0.5 7 3 Q8 0.5 11 0.5 Q15 1 13 5 Z" fill="#000"/></svg>
      <svg width="14" height="12" viewBox="0 0 14 12"><path d="M7 12 L1 5 Q-1 1 3 0.5 Q6 0.5 7 3 Q8 0.5 11 0.5 Q15 1 13 5 Z" fill="#000"/></svg>
      <svg width="14" height="12" viewBox="0 0 14 12"><path d="M7 12 L1 5 Q-1 1 3 0.5 Q6 0.5 7 3 Q8 0.5 11 0.5 Q15 1 13 5 Z" fill="#000"/></svg>
      <svg width="14" height="12" viewBox="0 0 14 12"><path d="M7 12 L1 5 Q-1 1 3 0.5 Q6 0.5 7 3 Q8 0.5 11 0.5 Q15 1 13 5 Z" fill="#000"/></svg>
      <svg width="14" height="12" viewBox="0 0 14 12"><path d="M7 12 L1 5 Q-1 1 3 0.5 Q6 0.5 7 3 Q8 0.5 11 0.5 Q15 1 13 5 Z" fill="#000"/></svg>
    </div>
  </div>

  <div class="you-me heavy abs">
    <span class="you">YOU</span><span class="divider"></span><span class="me">ME</span>
  </div>

  <div class="side-pennant abs">
    <svg viewBox="0 0 250 256" width="250" height="256">
      <polygon points="224,18 238,22 238,176 128,254 120,248 224,172" fill="url(#hatch)"/>
      <path d="M4 14 Q4 8 10 8 L224 8 L224 172 L122 248 L4 170 Z" fill="#fff" stroke="#000" stroke-width="3.5" stroke-linejoin="round"/>
      <path d="M206 8 L232 4 Q244 4 242 14 Q240 20 232 18 L224 16 L224 8 Z" fill="#000"/>
    </svg>
    <div class="pointing-hands" role="img" aria-label="Two hands pointing to the right"></div>
    <div class="pennant-rule"></div>
    <div class="pennant-text heavy">
      <span class="small">BY YOUR</span>
      <span class="big">SIDE</span>
    </div>
  </div>

  <svg class="triangle-row abs" style="top:1133px" width="705" height="16"><rect width="705" height="16" fill="url(#tri-up)"/></svg>

</main>
</body>
</html>
```